Construction company focused on concrete and shed construction.

We need to update our current business card for ridgeforgebuilds.com.au we would like an eye catching design with blue, grey and white incorporating our current logo.
Our company started off in concreting and due to varying factors we have expanded to include shed construction as well.
This has led to our current Logo looking a little out of place and somehow need to use the card to bring in the shed construction side of the business while not having to change current concrete look "KESTRO" logo as we already have this incorporated into our company clothing and are not willing to change this yet.
Photo image attached for inspiration/ visual reference of type of work, not to be used on final design.
Please no cheesy designs of men in hard hats and tools
Final design should demonstrate a modern and service focused company.

Target Market(s)

Farmers, Business owners, Developers, Architects, Commercial project delivery

Industry/Entity Type

Construction Company

Contact Information for Business Card

Kestro Constructions.
7b Harlow st
South Launceston Tas
03 62918873

Font styles to use
Other font styles liked:
• see font in logo

Colors
3176b5
b2b2b2

Requirements
Must have
• Easy to read font,
• good contrast between back ground and writing
Nice to have
• Modern and corporate look with a fun but professional image.
Should not have
• Comic images or shadow images of tools/ people.

```html
<!DOCTYPE html>
<html lang="en">
<head>
<meta charset="utf-8">
<title>Kestro Constructions – Business Card</title>
<link rel="stylesheet" href="https://fonts.googleapis.com/css2?family=Graduate&family=Roboto:wght@400;700&display=swap">
<style>
  :root {
    --backdrop: #d9dadc;
    --slate: #4a5862;
    --card-light: #ececec;
    --brand-blue: #3176b5;
    --brand-grey: #b2b2b2;
    --text-grey: #555a5f;
    --white: #ffffff;
  }
  html, body {
    margin: 0;
    padding: 0;
    width: 1200px;
    height: 780px;
    overflow: hidden;
    background: var(--backdrop);
    font-family: "Roboto", Arial, sans-serif;
  }
  .canvas {
    position: relative;
    width: 1200px;
    height: 780px;
  }
  .card {
    position: absolute;
    top: 235px;
    width: 540px;
    height: 310px;
    box-shadow: 0 6px 18px rgba(0,0,0,0.18);
  }
  /* Front */
  .card-front {
    left: 40px;
    background: var(--slate);
    color: var(--white);
    text-align: center;
  }
  .company-title {
    margin: 112px 0 0;
    font-family: "Graduate", "Roboto", serif;
    font-size: 38px;
    letter-spacing: 1px;
    line-height: 1;
  }
  .front-website {
    margin: 22px 0 0;
    font-size: 13px;
    letter-spacing: 3px;
    color: #dfe3e6;
  }
  /* Back */
  .card-back {
    left: 620px;
    background: var(--card-light);
    color: var(--text-grey);
  }
  .contact-block {
    position: absolute;
    left: 34px;
    top: 150px;
  }
  .person-name {
    margin: 0;
    font-size: 17px;
    font-weight: 700;
    color: var(--brand-blue);
    letter-spacing: 0.5px;
  }
  .person-role {
    margin: 1px 0 12px;
    font-size: 12px;
    color: var(--text-grey);
  }
  .contact-line {
    display: flex;
    align-items: center;
    gap: 6px;
    margin: 0 0 4px;
    font-size: 12.5px;
    white-space: nowrap;
  }
  .contact-line svg { flex: none; }
  .divider { color: var(--brand-blue); margin: 0 4px; }
  .brand-mark {
    position: absolute;
    right: 40px;
    top: 62px;
    display: flex;
    align-items: center;
    gap: 8px;
  }
  .brand-dot {
    width: 22px;
    height: 22px;
    border-radius: 50%;
    background: var(--brand-blue);
  }
  .brand-name {
    font-size: 26px;
    font-weight: 700;
    color: var(--brand-blue);
    letter-spacing: 1px;
  }
  .social-row {
    position: absolute;
    right: 40px;
    bottom: 26px;
    display: flex;
    gap: 8px;
  }
  .social-slot {
    width: 20px;
    height: 20px;
    border-radius: 3px;
    background: var(--brand-grey);
  }
</style>
</head>
<body>
<main class="canvas">
  <section class="card card-front">
    <h1 class="company-title">KESTRO CONSTRUCTIONS</h1>
    <p class="front-website">ridgeforgebuilds.com.au</p>
  </section>

  <section class="card card-back">
    <div class="brand-mark">
      <span class="brand-dot"></span>
      <span class="brand-name">KESTRO</span>
    </div>

    <div class="contact-block">
      <h2 class="person-name">LIAM CARTER</h2>
      <p class="person-role">Project Manager</p>
      <p class="contact-line">
        <svg width="13" height="13" viewBox="0 0 13 13"><circle cx="6.5" cy="6.5" r="5.8" fill="none" stroke="#3176b5" stroke-width="1.2"/><path d="M4.6 3.6 L5.6 5.2 L5 5.9 Q5.8 7.5 7.1 8 L7.8 7.4 L9.4 8.4 Q8.7 9.7 7.4 9.3 Q4.3 8.2 3.7 5.4 Q3.5 4.2 4.6 3.6Z" fill="#3176b5"/></svg>
        03 62918873<span class="divider">|</span>
        <svg width="13" height="13" viewBox="0 0 13 13"><circle cx="6.5" cy="6.5" r="5.8" fill="none" stroke="#3176b5" stroke-width="1.2"/><rect x="3.5" y="4.5" width="6" height="4" fill="#3176b5"/></svg>
        admin@ridgeforgebuilds.com.au
      </p>
      <p class="contact-line">
        <svg width="13" height="13" viewBox="0 0 13 13"><circle cx="6.5" cy="6.5" r="5.8" fill="none" stroke="#3176b5" stroke-width="1.2"/><circle cx="6.5" cy="6.5" r="3.5" fill="none" stroke="#3176b5"/><path d="M3 6.5 H10 M6.5 3 V10" stroke="#3176b5"/></svg>
        ridgeforgebuilds.com.au
      </p>
      <p class="contact-line">
        <svg width="13" height="13" viewBox="0 0 13 13"><circle cx="6.5" cy="6.5" r="5.8" fill="none" stroke="#3176b5" stroke-width="1.2"/><path d="M6.5 10 L4.4 6.6 A2.4 2.4 0 1 1 8.6 6.6 Z" fill="#3176b5"/></svg>
        7b Harlow st. South Launceston Tas
      </p>
    </div>

    <div class="social-row">
      <span class="social-slot"></span>
      <span class="social-slot"></span>
      <span class="social-slot"></span>
    </div>
  </section>
</main>
</body>
</html>
```